Brochure about Gun Trusts

Cover Page: Image of a firearm collection or a lockbox with the title]
Headline: Protect Your Firearms Collection with a Gun Trust
Subheading: Ensure Your Legacy Remains Private and Your Wishes Are Respected
[Page 1: What is a Gun Trust?]
Definition: A legally recognized trust that allows you to collect, own, and transfer firearms, including those restricted by the NFA.
Quote: "A gun trust is a revocable trust created to hold ownership of a firearm..." - KMW
[Page 2: Benefits of a Gun Trust]
Avoid Probate: Keep your firearms out of the public probate process, maintaining your privacy.
Multi-Generational Ownership: Easily transfer ownership to beneficiaries without the need for a court proceeding.
Shared Responsibility: Allow others to legally possess and use the firearms held in the trust.
[Page 3: The Risks of Not Having a Gun Trust]
Inheritance Issues: Firearms may not be transferred as intended, potentially leading to legal complications.
Probate and Public Disclosure: Your firearms collection becomes a public record.
[Page 4: How to Set Up a Gun Trust]
Consult with an Attorney: A firearms trust attorney will create a trust that complies with all federal and state laws.
Assign a Trustee: Choose a trustee to manage the trust if you become incapacitated or pass away.
Transfer Ownership: Assign your firearms to the trust.
[Back Cover: Call to Action]
Headline: Protect Your Firearms Legacy
Contact Information: Address, Phone Number, Email, Website
Offer: Free Consultation to discuss your options

```html
<!DOCTYPE html>
<html lang="en">
<head>
<meta charset="utf-8">
<title>Gun Trust Brochure</title>
<link href="https://fonts.googleapis.com/css2?family=Anton&family=Poppins:wght@400;500;600;700;800&display=swap" rel="stylesheet">
<style>
:root{
  --bg:#a2a2a2;
  --black:#0d0d0d;
  --dark:#1c1c1c;
  --yellow:#fdb813;
  --orange:#f7941d;
  --white:#ffffff;
  --ink:#1a1a1a;
  --rule:#8a8a8a;
}
*{margin:0;padding:0;box-sizing:border-box}
html,body{width:1200px;height:2292px;overflow:hidden;background:var(--bg)}
body{position:relative;font-family:'Poppins',sans-serif;color:var(--ink)}
.page{position:absolute;width:481px;height:623px;overflow:hidden;box-shadow:0 6px 14px rgba(0,0,0,.35)}
.p-cover{left:94px;top:151px;background:var(--black)}
.p-back{left:625px;top:151px;background:var(--black)}
.p-what{left:94px;top:830px;background:var(--white)}
.p-benefits{left:625px;top:830px;background:var(--white)}
.p-risks{left:94px;top:1517px;background:var(--white)}
.p-setup{left:625px;top:1517px;background:var(--white)}
.abs{position:absolute}
.photo{position:absolute}
.torn-v{clip-path:polygon(2% 0,98% 0,96% 6%,99% 12%,97% 19%,100% 27%,97% 35%,99% 44%,96% 52%,99% 61%,97% 70%,100% 80%,97% 90%,99% 100%,1% 100%,4% 91%,0 82%,3% 72%,1% 62%,4% 53%,0 43%,3% 34%,1% 25%,4% 16%,0 8%)}
.kicker{font-weight:700;letter-spacing:6px;font-size:19px;text-align:center;width:100%}
.cover-title{font-weight:800;font-size:37px;line-height:38px;text-align:center;width:100%}
.display{font-family:'Anton',sans-serif;text-transform:uppercase;letter-spacing:-1px}
.site{font-size:19px;letter-spacing:3px;color:var(--yellow);text-align:center;width:100%}
.site b{font-weight:700}
.footer-site{position:absolute;top:570px;left:38px;font-size:10.5px;letter-spacing:1.6px}
.footer-rule{position:absolute;top:577px;height:1px;background:var(--rule)}
.page-num{position:absolute;top:567px;width:24px;height:60px;border-radius:12px 12px 0 0;background:var(--yellow);font-size:7px;font-weight:700;text-align:center;padding-top:11px}
.pill{position:absolute;left:41px;width:161px;height:35px;border-radius:18px;display:flex;align-items:center;font-size:14px;font-weight:500}
.pill .ico,.card .ico{width:35px;height:35px;border-radius:50%;background:var(--dark);border:2px solid var(--white);margin-right:12px;flex:none;display:flex;align-items:center;justify-content:center}
.card{position:absolute;border-radius:16px;padding:14px 12px;display:flex;align-items:flex-start;font-size:12.6px;line-height:15px}
.card .ico{margin-right:11px;margin-top:2px}
.card b{display:block;font-weight:700}
.y{background:var(--yellow)}
.o{background:var(--orange)}
.contact{position:absolute;left:0;width:100%;text-align:center;font-size:11.5px;font-weight:600}
.dot{position:absolute;left:50%;margin-left:-9px;width:18px;height:18px;border-radius:50%;background:var(--black);display:flex;align-items:center;justify-content:center}
</style>
</head>
<body>

<!-- Cover -->
<section class="page p-cover">
  <div class="photo" role="img" aria-label="Dark wooden table texture" style="inset:0;background:radial-gradient(ellipse at 50% 70%,#2a2622,#050505 75%)"></div>
  <div class="abs torn-v" style="left:84px;top:0;width:317px;height:470px;background:linear-gradient(#fdb813,#f5a800)"></div>
  <div class="photo" role="img" aria-label="Pistol with brass cartridges on a wooden table" style="left:60px;top:290px;width:400px;height:290px;background:radial-gradient(ellipse at 55% 45%,#7b6a55 0%,#3c2f25 45%,rgba(10,10,10,0) 75%)"></div>
  <p class="abs kicker" style="top:38px;color:var(--black)">PROTECT YOUR</p>
  <h1 class="abs cover-title" style="top:69px;color:var(--black)">FIREARMS<br>COLLECTION</h1>
  <div class="abs display" style="left:90px;top:151px;width:300px;height:62px;background:var(--black);color:var(--white);font-size:45px;line-height:62px;text-align:center">With Gun Trust</div>
  <p class="abs" style="top:224px;width:100%;text-align:center;font-size:13.5px;font-weight:600;line-height:17px;color:var(--black)">Ensure Your Legacy Remains<br>Private and Your Wishes Are<br>Respected</p>
  <p class="abs site" style="top:560px">www.<b>holdtrust</b>.com</p>
</section>

<!-- Back cover -->
<section class="page p-back">
  <div class="photo" role="img" aria-label="Silver pistol on dark surface with scattered cartridges" style="inset:0;background:radial-gradient(ellipse at 60% 40%,#4a4a4a,#111 50%,#000 80%)"></div>
  <div class="abs torn-v" style="left:114px;top:300px;width:254px;height:330px;background:var(--yellow)"></div>
  <p class="abs kicker" style="top:38px;color:var(--white)">PROTECT YOUR</p>
  <h1 class="abs cover-title" style="top:69px;color:var(--yellow)">FIREARMS<br>LEGACY</h1>
  <div class="abs display" style="top:354px;width:100%;padding-left:24px;text-align:center;font-size:28px;color:var(--black)">Free Consultation</div>
  <p class="abs" style="top:387px;width:100%;padding-left:24px;text-align:center;font-size:10.5px;font-weight:600;letter-spacing:2.4px">TO DISCUSS YOUR OPTIONS</p>
  <div class="dot" style="top:410px;margin-left:-2px"><svg width="10" height="10" viewBox="0 0 10 10"><path d="M2 1l2 2-1 1c.6 1.3 1.7 2.4 3 3l1-1 2 2-1.5 1.5C4.500 8.500 1.500 5.500 .500 2.500z" fill="#fdb813"/></svg></div>
  <p class="contact" style="top:432px;padding-left:16px">555 0142 7788</p>
  <div class="dot" style="top:454px;margin-left:-2px"><svg width="10" height="8" viewBox="0 0 10 8"><rect x=".5" y=".5" width="9" height="7" fill="none" stroke="#fdb813"/><path d="M.5 .5l4.500 4 4.500-4" fill="none" stroke="#fdb813"/></svg></div>
  <p class="contact" style="top:474px;padding-left:16px">info@holdtrust.com</p>
  <div class="dot" style="top:498px;margin-left:-2px"><svg width="8" height="11" viewBox="0 0 8 11"><path d="M4 11C1 7 0 5.500 0 4a4 4 0 018 0c0 1.500-1 3-4 7z" fill="#fdb813"/><circle cx="4" cy="4" r="1.400" fill="#0d0d0d"/></svg></div>
  <p class="contact" style="top:519px;padding-left:16px;line-height:13px">Harbor City, Stateville<br>80214</p>
  <p class="abs site" style="top:563px;color:var(--black);font-size:15px;padding-left:16px">www.<b>holdtrust</b>.com</p>
</section>

<!-- What is -->
<section class="page p-what">
  <div class="abs" style="left:0;top:0;width:100%;height:262px;background:var(--yellow);clip-path:polygon(0 0,100% 0,100% 100%,90% 98%,78% 100%,64% 97%,50% 99%,35% 97%,20% 100%,8% 98%,0 100%)"></div>
  <div class="abs" style="left:0;top:0;width:100%;height:256px;background:linear-gradient(90deg,#050505,#2a2a2a);clip-path:polygon(0 0,100% 0,100% 98%,88% 96%,75% 99%,60% 95%,46% 98%,30% 95%,16% 99%,0 96%)"></div>
  <div class="photo" role="img" aria-label="Heavy brass and steel padlock" style="left:279px;top:6px;width:170px;height:231px;background:radial-gradient(ellipse at 50% 55%,#8a7346,#3b3324 50%,rgba(0,0,0,0) 72%)"></div>
  <h2 class="abs display" style="left:37px;top:34px;font-size:53px;line-height:58px;color:var(--white)">What is<br><span style="color:var(--yellow)">A Gun<br>Trust?</span></h2>
  <p class="abs" style="left:41px;top:297px;font-size:17px;font-weight:600;line-height:21px">A legally<br>recognized trust<br>that allows you to</p>
  <div class="pill y" style="top:388px"><span class="ico"><svg width="14" height="10" viewBox="0 0 14 10"><path d="M1 2h12v3H6l-1 4H2l1-4H1z" fill="#fff"/></svg></span>Collect</div>
  <div class="pill o" style="top:435px"><span class="ico"><svg width="14" height="12" viewBox="0 0 14 12"><circle cx="5" cy="3" r="2.200" fill="#fff"/><path d="M1 12c0-4 8-4 8 0z" fill="#fff"/><rect x="8" y="4" width="6" height="2" fill="#fff"/></svg></span>Own</div>
  <div class="pill y" style="top:481px"><span class="ico"><svg width="14" height="14" viewBox="0 0 14 14"><circle cx="7" cy="7" r="5.500" fill="none" stroke="#fff" stroke-width="1.500"/><path d="M4 7h6M8 5l2 2-2 2" fill="none" stroke="#fff" stroke-width="1.500"/></svg></span>Transfer</div>
  <p class="abs" style="left:251px;top:293px;font-size:16px;font-weight:700;letter-spacing:3px;color:var(--orange)">FIREARMS</p>
  <p class="abs" style="left:251px;top:312px;font-size:12px;font-weight:600;line-height:15px">including those restricted<br>by the NFA.</p>
  <div class="abs" style="left:251px;top:358px;width:157px;height:1px;background:var(--rule)"></div>
  <div class="abs" style="left:251px;top:385px;width:173px;height:150px;border-radius:12px;background:var(--black);color:var(--white);padding:20px 16px;font-size:15px;font-weight:600;line-height:20px">A gun trust is a revocable trust created to hold ownership of a firearm...<span style="display:block;color:var(--yellow);font-size:14px;font-weight:700;margin-top:2px">KMW</span></div>
  <span class="abs display" style="left:262px;top:352px;font-size:54px;line-height:54px;color:var(--yellow)">“</span>
  <span class="abs display" style="left:380px;top:514px;font-size:54px;line-height:54px;color:var(--yellow)">”</span>
  <div class="photo" role="img" aria-label="Scattered brass bullet cartridges" style="left:425px;top:280px;width:56px;height:270px;background:linear-gradient(180deg,rgba(230,180,40,.5),rgba(230,180,40,.15),rgba(230,180,40,.5))"></div>
  <p class="footer-site">www.holdtrust.com</p>
  <div class="footer-rule" style="left:173px;width:230px"></div>
  <div class="page-num" style="left:415px">1</div>
</section>

<!-- Benefits -->
<section class="page p-benefits">
  <div class="abs" style="left:300px;top:0;width:181px;height:100%;background:var(--yellow);clip-path:polygon(3% 0,100% 0,100% 100%,5% 100%,0 88%,4% 75%,1% 60%,5% 45%,0 30%,4% 15%)"></div>
  <div class="photo" role="img" aria-label="Two people shaking hands over a signed document beside a scale of justice" style="left:306px;top:0;width:175px;height:100%;background:linear-gradient(180deg,#161616,#2a241f 40%,#6b5a4a 60%,#1a1a1a 90%)"></div>
  <h2 class="abs display" style="left:38px;top:38px;font-size:53px;line-height:56px;color:var(--ink)">Benefits<br>of a<br><span style="color:var(--orange)">Gun Trust</span></h2>
  <div class="card y" style="left:41px;top:221px;width:270px;height:93px"><span class="ico"><svg width="16" height="14" viewBox="0 0 16 14"><path d="M8 1v12M3 13h10M2 3h12M2 3l-2 5h4zM14 3l-2 5h4z" fill="none" stroke="#fff"/></svg></span><div><b>Avoid Probate:</b>Keep your firearms out of the public probate process, maintaining your privacy.</div></div>
  <div class="card o" style="left:41px;top:324px;width:270px;height:92px"><span class="ico"><svg width="16" height="14" viewBox="0 0 16 14"><rect x="2" y="2" width="12" height="10" fill="none" stroke="#fff"/><circle cx="8" cy="7" r="2" fill="#fff"/></svg></span><div><b>Multi-Generational Ownership:</b>Easily transfer ownership to beneficiaries without the need for a court proceeding.</div></div>
  <div class="card y" style="left:41px;top:425px;width:270px;height:94px"><span class="ico"><svg width="16" height="16" viewBox="0 0 16 16"><circle cx="8" cy="8" r="6" fill="none" stroke="#fff"/><circle cx="8" cy="6" r="2" fill="#fff"/><path d="M4 12c1-3 7-3 8 0" fill="none" stroke="#fff"/></svg></span><div><b>Shared Responsibility:</b>Allow others to legally possess and use the firearms held in the trust.</div></div>
  <p class="footer-site">www.holdtrust.com</p>
  <div class="footer-rule" style="left:173px;width:116px"></div>
  <div class="page-num" style="left:415px">2</div>
</section>

<!-- Risks -->
<section class="page p-risks">
  <div class="abs" style="left:0;top:0;width:222px;height:100%;background:var(--yellow);clip-path:polygon(0 0,98% 0,95% 12%,100% 25%,96% 38%,99% 52%,95% 66%,100% 80%,96% 92%,99% 100%,0 100%)"></div>
  <div class="photo" role="img" aria-label="Hands around a wobbling wooden block tower with a pistol below" style="left:0;top:0;width:215px;height:100%;background:linear-gradient(160deg,#4a2410,#1e120c 45%,#2b2018 70%,#0a0a0a)"></div>
  <h2 class="abs display" style="left:233px;top:40px;font-size:36px;line-height:38px;color:var(--ink)">The Risks of<br>Not Having a<br><span style="color:var(--orange);font-size:57px;line-height:58px">Gun<br>Trust</span></h2>
  <div class="card y" style="left:215px;top:252px;width:226px;height:105px;border-radius:0 16px 16px 0"><span class="ico"><svg width="16" height="14" viewBox="0 0 16 14"><path d="M8 1v12M3 13h10M2 3h12M2 3l-2 5h4zM14 3l-2 5h4z" fill="none" stroke="#fff"/></svg></span><div><b>Inheritance Issues:</b>Firearms may not be transferred as intended, potentially leading to legal complications.</div></div>
  <div class="card o" style="left:215px;top:368px;width:226px;height:105px;border-radius:0 16px 16px 0"><span class="ico"><svg width="14" height="16" viewBox="0 0 14 16"><rect x="2" y="1" width="10" height="14" fill="none" stroke="#fff"/><path d="M4 5h6M4 8h6M4 11h4" stroke="#fff"/></svg></span><div><b>Probate and Public Disclosure:</b>Your firearms collection becomes a public record.</div></div>
  <div class="photo" role="img" aria-label="Scattered brass bullet cartridges" style="left:250px;top:505px;width:231px;height:118px;background:radial-gradient(ellipse at 50% 50%,rgba(230,180,40,.35),rgba(255,255,255,0) 70%)"></div>
  <p class="footer-site" style="color:var(--white)">www.holdtrust.com</p>
  <div class="footer-rule" style="left:237px;width:170px"></div>
  <div class="page-num" style="left:415px">3</div>
</section>

<!-- How to set up -->
<section class="page p-setup">
  <div class="abs" style="left:0;top:305px;width:100%;height:318px;background:var(--yellow);clip-path:polygon(0 2%,12% 0,26% 2%,40% 0,55% 2%,70% 0,85% 2%,100% 0,100% 100%,0 100%)"></div>
  <div class="abs" style="left:0;top:311px;width:100%;height:312px;background:linear-gradient(160deg,#262626,#0a0a0a);clip-path:polygon(0 2%,14% 0,29% 2%,44% 0,58% 2%,73% 0,88% 2%,100% 0,100% 100%,0 100%)"></div>
  <div class="photo" role="img" aria-label="Golden scale of justice on a marble base" style="left:301px;top:342px;width:155px;height:213px;background:radial-gradient(ellipse at 50% 60%,#7a6430,#2c2614 45%,rgba(0,0,0,0) 72%)"></div>
  <h2 class="abs display" style="left:38px;top:50px;font-size:40px;line-height:46px;color:var(--ink)">How to<br>Set up a<br><span style="color:var(--orange);font-size:60px;line-height:66px">Gun<br>Trust</span></h2>
  <div class="card y" style="left:219px;top:53px;width:222px;height:105px"><span class="ico"><svg width="16" height="14" viewBox="0 0 16 14"><path d="M8 1v12M3 13h10M2 3h12M2 3l-2 5h4zM14 3l-2 5h4z" fill="none" stroke="#fff"/></svg></span><div><b>Assign a Trustee:</b>Choose a trustee to manage the trust if you become incapacitated or pass away.</div></div>
  <div class="card o" style="left:219px;top:170px;width:222px;height:105px"><span class="ico"><svg width="14" height="16" viewBox="0 0 14 16"><rect x="2" y="1" width="10" height="14" fill="none" stroke="#fff"/><path d="M4 5h6M4 8h6M4 11h4" stroke="#fff"/></svg></span><div><b>Transfer Ownership:</b>Assign your firearms to the trust.</div></div>
  <p class="abs display" style="left:38px;top:352px;font-size:27px;line-height:29px;color:var(--yellow);text-transform:none">Consult with an<br>Attorney:</p>
  <p class="abs" style="left:38px;top:432px;width:195px;font-size:14px;line-height:18.5px;color:var(--white)">A firearms trust attorney will create a trust that complies with all federal and state laws.</p>
  <p class="footer-site" style="color:var(--white);left:42px">www.holdtrust.com</p>
  <div class="footer-rule" style="left:176px;width:236px"></div>
  <div class="page-num" style="left:415px">4</div>
</section>

</body>
</html>
```